Business Card Design

We are a new residential construction company.our team is made up of young highly skilled tradesman of the next generation of carpenters coming through with new skills and ideas.we chose the name meridian as it means strikingly different from the rest as this is what we plan to be and we would like to portray this in our business card.we like Bold lettering as we want to make a statement, also the use of colour would be great as we want to stand out from the usual plain construction cards and logos.
I have attached a logo sketch I did as a rough idea if you can tidy it up or improve on it would be good.
I have also attached the LBP logo please include this on the card small but still legible.
open to any colourschemes ideas.
thanks
(note)please delete the LBP#308617 off from the card details please.
Updates
Industry/Entity Type
Construction
Contact Information for Business Card
MERIDIAN CONSTRUCTION LIMITED
Director:Kai Pereira
Mobile :0217364801
Email:Meridian.Construction@examplemail.test
Address:48 Halvorsen place,Ashgrove park 2071,Auckland
LBP#BP308617
Look and feel
Each slider illustrates characteristics of the customer's brand and the style your logo design should communicate.

```html
<!DOCTYPE html>
<html lang="en">
<head>
<meta charset="utf-8">
<title>Meridian Construction Limited – Business Card</title>
<link rel="stylesheet" href="https://fonts.googleapis.com/css2?family=Archivo:wght@800&family=Archivo+Narrow:wght@700&family=Noto+Serif:wght@700&display=swap">
<style>
  :root {
    --page-bg: #e9e7e3;
    --card-white: #ffffff;
    --ink: #0b0b0b;
    --band-black: #000000;
    --band-text: #f4f4f4;
    --badge-rim: #9a9a9a;
  }
  * { box-sizing: border-box; margin: 0; padding: 0; }
  html, body {
    width: 1200px;
    height: 900px;
    overflow: hidden;
    background: var(--page-bg);
  }
  .canvas {
    position: relative;
    width: 1200px;
    height: 900px;
  }
  .business-card {
    position: absolute;
    left: 100px;
    top: 140px;
    width: 1000px;
    height: 620px;
    background: var(--card-white);
    overflow: hidden;
    box-shadow: 0 2px 10px rgba(0,0,0,0.15);
  }
  .lbp-badge {
    position: absolute;
    left: 84px;
    top: 47px;
    width: 120px;
    height: 120px;
  }
  .company-name {
    position: absolute;
    left: 64px;
    top: 193px;
    font-family: "Archivo", "Arial Black", sans-serif;
    font-weight: 800;
    font-size: 40px;
    letter-spacing: 0.5px;
    color: var(--ink);
    white-space: nowrap;
  }
  .director-name {
    position: absolute;
    left: 70px;
    top: 246px;
    font-family: "Archivo Narrow", "Arial Narrow", sans-serif;
    font-weight: 700;
    font-size: 37px;
    color: var(--ink);
  }
  .contact-band {
    position: absolute;
    left: 0;
    bottom: 0;
    width: 100%;
    height: 184px;
    background: var(--band-black);
  }
  .contact-list {
    position: absolute;
    left: 488px;
    top: 28px;
    list-style: none;
    font-family: "Noto Serif", Georgia, serif;
    font-weight: 700;
    font-size: 16px;
    line-height: 36px;
    color: var(--band-text);
    white-space: nowrap;
  }
</style>
</head>
<body>
<main class="canvas">
  <article class="business-card">
    <svg class="lbp-badge" viewBox="0 0 120 120" aria-hidden="true">
      <circle cx="60" cy="60" r="58" fill="var(--card-white)" stroke="var(--badge-rim)" stroke-width="2"/>
      <circle cx="60" cy="60" r="44" fill="var(--ink)"/>
    </svg>
    <h1 class="company-name">MERIDIAN CONSTRUCTION LIMITED</h1>
    <p class="director-name">Kai Pereira</p>
    <section class="contact-band">
      <ul class="contact-list">
        <li>Mobile : 0217364801</li>
        <li>Email : Meridian.Construction@examplemail.test</li>
        <li>Address : 48 Halvorsen place,Ashgrove park 2071,Auckland</li>
      </ul>
    </section>
  </article>
</main>
</body>
</html>
```